Lagoon Canopy NZ Product Catalogue

To redesign our suppliers catalogue and make it my own.
Verdmont is our supplier, although now I want a "Lagoon Canopy NZ" catalogue, with an updated look as well.

I have attached our logos, Verdmont catalogue and a few photos of completed work (which may need editing to look better).

Also pages I want to use from the catalogue (be similar to) are page numbers:
10 - 21 (products we sell)
It will also need a cover and contents page and a commercial enclosure page after the other products (with commercial 1 and 20130422_1 photos).

The first page as you open the catalogue I want the about us section of our website on there www.lagooncanopy.co.nz (two sections "what we offer" and "enclosure advantages")

If you need better photos or more information please contact me on:
tamsin@lagooncanopy.co.nz

Contact details: Toll Free 0508 SHELTERS (748 219) Email sales@lagooncanopy.co.nz

Industry/Entity Type

Construction

Colors

Designer to choose colors to be used in the design.

Requirements
Must have
• Must have double sided pages,
• With each different design to have two pages which open together.
• The standard sizing which is in the Verdmont Catalogue must be there.
• Designs are: Rivelle Horizon, Rivelle, Tormel, Quarry, Lisbet and Vale Shelters
• Must be printable and pdf sendable.
• Use "What we offer" and "Enclosure Advantages" to the first page customer opens to, maybe also a contents page.
• Also please add to the "enclosure advantages" bullet point list "Year-round average of 8 degree warmer water"
Nice to have
• Would be nice to have the custom sizing box as well on the designs asked for.
• Also a Commercial section after the rest of the designs using the "commercial 1" and "20130422_1" photos
• The more photos the better
• Be nice to be high resolution and I want to print it in a gloss finish.
• Also A4 size would be nice, but A5 will work also
Should not have
• Rivelle Horizon Neo and try and minimise the Verdmont branding

```html
<!DOCTYPE html>
<html lang="en">
<head>
<meta charset="utf-8">
<title>Lagoon Canopy NZ – Catalogue Spreads</title>
<link rel="stylesheet" href="https://fonts.googleapis.com/css2?family=Open+Sans:wght@300;400;700;800&family=Ubuntu:wght@300;500;700&display=swap">
<style>
  :root{
    --bg:#111214;
    --paper:#ffffff;
    --brand-blue:#1b5fc9;
    --deep-blue:#1c4fb5;
    --cyan:#5ccfdf;
    --cyan-soft:#bff0f4;
    --cyan-head:#86dde7;
    --ink:#333c48;
    --rule:#2d5fc2;
  }
  *{box-sizing:border-box;margin:0;padding:0}
  html,body{width:1200px;height:1200px;overflow:hidden;background:var(--bg)}
  body{position:relative;font-family:"Open Sans",Arial,sans-serif;color:var(--ink)}

  .spread{position:absolute;width:585px;height:414px;background:var(--paper);overflow:hidden}
  .spread--lisbet{left:8px;top:166px}
  .spread--quarry{left:607px;top:166px}
  .spread--vale{left:307px;top:620px}

  .header-band{position:absolute;left:0;top:0;width:67.4%;height:10.2%;
    background:linear-gradient(90deg,#1f68cf 0%,#36a9e0 40%,#6fd9e2 75%,#9ae8e6 100%)}
  .title-tab{position:absolute;left:0;top:0;width:26%;height:10.2%;background:var(--paper);
    border-bottom-right-radius:22px;border-right:4px solid var(--brand-blue)}
  .page-title{position:absolute;left:6%;top:1.6%;font-family:"Ubuntu",sans-serif;font-weight:700;
    font-size:18px;letter-spacing:.5px;color:var(--brand-blue);text-transform:uppercase}
  .page-title--stacked{top:.6%;line-height:.95;font-size:16px}
  .page-title--stacked .light{display:block;font-weight:300}

  .photo{position:absolute;background:linear-gradient(160deg,#8fc6ea 0%,#5fb6d8 40%,#4f8f5a 75%,#7a9a55 100%)}
  .photo--pool{background:linear-gradient(170deg,#9fd0f0 0%,#6cc6ea 35%,#3aa7e0 60%,#2a74c9 100%)}
  .photo--garden{background:linear-gradient(170deg,#c8dce8 0%,#8aac6a 45%,#5c8c3a 100%)}
  .photo--water{background:linear-gradient(180deg,#d8e6ee 0%,#9cc0d6 45%,#3f6a8f 75%,#8a6a4a 100%)}
  .photo--terrace{background:linear-gradient(170deg,#bcd7ea 0%,#8fb07a 50%,#9a8a78 100%)}

  .hero{left:0;top:10.2%;width:67.4%;height:55.4%}
  .side-top{left:68%;top:0;width:32%;height:20%}
  .row-a{left:0;top:66.2%;width:40.2%;height:23%}
  .row-b{left:40.5%;top:66.2%;width:26.9%;height:23%}
  .row-c{left:68%;top:66.2%;width:32%;height:23%}

  .info-box{position:absolute;left:69%;top:21.4%;width:30%;height:14%;background:var(--cyan-soft);
    border-radius:3px;padding:3px 5px;text-align:center}
  .info-title{font-family:"Ubuntu",sans-serif;font-weight:500;font-size:9.5px;color:var(--cyan);
    text-transform:uppercase;letter-spacing:.3px;line-height:1.1}
  .info-text{font-size:4.4px;line-height:1.45;color:#2e3944;margin-top:1px}
  .info-text b{font-weight:700}

  .diagram{position:absolute;left:70%;top:36.2%;width:28%;height:8.6%;
    background:linear-gradient(90deg,#e6e9ee,#f6f1f6);border-radius:2px}

  .spec-table{position:absolute;left:69.2%;width:29.8%;border-collapse:collapse;font-size:4.2px;line-height:1.25}
  .spec-table td,.spec-table th{border:.6px solid var(--rule);padding:.6px 2px;text-align:left;font-weight:400}
  .spec-table th{font-weight:700;color:#fff;text-transform:uppercase}
  .spec-table--custom{top:45.6%}
  .spec-table--custom th{background:var(--deep-blue)}
  .spec-table--standard{top:55%}
  .spec-table--standard th{background:var(--cyan-head);border-color:var(--cyan-head);vertical-align:top}
  .spec-table--standard td{border-color:#c9e9ee}

  .footer{position:absolute;left:0;top:89.2%;width:100%;height:10.8%;background:var(--paper)}
  .page-no{position:absolute;top:0;width:16px;height:5px;background:var(--brand-blue);color:#fff;
    font-size:3.6px;line-height:5px;text-align:center}
  .page-no--left{left:0}
  .page-no--right{right:0}
  .brand-mark{position:absolute;right:4%;top:30%;display:flex;align-items:center;gap:4px;
    font-family:"Open Sans",sans-serif;font-weight:800;font-size:10px;color:var(--brand-blue);
    text-transform:uppercase;letter-spacing:.2px}
  .brand-mark .dot{width:7px;height:7px;border-radius:50%;background:var(--cyan)}

  /* Lisbet layout */
  .spread--lisbet .hero{width:67.4%}
  .spread--lisbet .row-a{width:33.4%}
  .spread--lisbet .row-b{left:33.7%;width:33.7%}
  .spread--lisbet .info-box{top:21.4%;height:14.6%}
  .spread--lisbet .spec-table--standard{top:46.5%}
  .lisbet-bottom{left:68%;top:62%;width:32%;height:27.2%}

  /* Vale layout */
  .spread--vale .hero{height:55.4%}
  .spread--vale .side-top{height:24.6%}
  .spread--vale .info-box{top:25.6%;height:9.8%}
  .vale-mid{left:68%;top:36%;width:32%;height:30%}
</style>
</head>
<body>

<!-- Lisbet spread -->
<section class="spread spread--lisbet" aria-label="Lisbet enclosure spread">
  <div class="header-band"></div>
  <div class="title-tab"></div>
  <h2 class="page-title">Lisbet</h2>

  <div class="photo photo--pool hero" role="img" aria-label="Interior view of a tall arched Lisbet enclosure over a long pool"></div>
  <div class="photo photo--garden side-top" role="img" aria-label="Lisbet enclosure over a pool in a landscaped garden"></div>

  <div class="info-box">
    <h3 class="info-title">Lisbet</h3>
    <p class="info-text">Lisbet is characteristic with its original and attractive design. <b>Dividing the frame in a dome</b> and a straight section increases the utility properties of the enclosure and improves its functions. The advantage of this type is its <b>sufficient height to comfortably walk</b> along the entire pool length, allowing a <b>pleasant time</b> near the pool after use, even if the weather is unfavorable.</p>
  </div>
  <div class="diagram" role="img" aria-label="Technical drawing of the Lisbet enclosure shape and height profile"></div>

  <table class="spec-table spec-table--standard">
    <tr><th colspan="2">Dimensions of standard enclosures</th></tr>
    <tr><td>Width</td><td>from 201 to 750 cm</td></tr>
    <tr><td>Height</td><td>from 105 to 350 cm</td></tr>
    <tr><td>Length</td><td>unlimited</td></tr>
  </table>

  <div class="photo photo--terrace lisbet-bottom" role="img" aria-label="Lisbet enclosure beside a terrace and lawn"></div>
  <div class="photo photo--garden row-a" role="img" aria-label="Rounded Lisbet enclosure next to a house"></div>
  <div class="photo photo--terrace row-b" role="img" aria-label="Lisbet enclosure by a timber deck with loungers"></div>

  <footer class="footer">
    <span class="page-no page-no--left">12</span>
    <span class="page-no page-no--right">13</span>
  </footer>
</section>

<!-- Quarry spread -->
<section class="spread spread--quarry" aria-label="Quarry enclosure spread">
  <div class="header-band"></div>
  <div class="title-tab"></div>
  <h2 class="page-title">Quarry</h2>

  <div class="photo photo--pool hero" role="img" aria-label="Low rounded Quarry enclosure with brown frame over a garden pool"></div>
  <div class="photo photo--garden side-top" role="img" aria-label="Quarry enclosure with side entrance beside a house"></div>

  <div class="info-box">
    <h3 class="info-title">Quarry</h3>
    <p class="info-text">If you like <b>round shapes and graceful curves</b> the Quarry pool enclosure is the best solution for you. Thanks to its elegant design, this enclosure is one of the most popular shapes and <b>fits into any garden.</b> If you're envisioning a <b>low enclosure</b> and love the fluidity of a rounded design, check out Quarry. Its <b>side entrance, top-quality insulating roofing material,</b> and <b>removable front panel</b> guarantee simple functionality.</p>
  </div>
  <div class="diagram" role="img" aria-label="Technical drawing of the Quarry enclosure shape and height profile"></div>

  <table class="spec-table spec-table--custom">
    <tr><th colspan="2">Dimensions of custom-made enclosures</th></tr>
    <tr><td>Width</td><td>from 251 to 800 cm</td></tr>
    <tr><td>Height</td><td>from 61 to 364 cm</td></tr>
    <tr><td>Length</td><td>unlimited</td></tr>
  </table>

  <table class="spec-table spec-table--standard">
    <tr><th>Dimensions of standard enclosures</th><th>Quarry A / Quarry Clear A</th><th>Quarry B / Quarry Clear B</th></tr>
    <tr><td>Outer width</td><td>407 cm</td><td>520 cm</td></tr>
    <tr><td>Inner width</td><td>379 cm</td><td>478 cm</td></tr>
    <tr><td>Outer length</td><td>646 cm</td><td>860 cm</td></tr>
    <tr><td>Outer height</td><td>75 cm</td><td>85 cm</td></tr>
  </table>

  <div class="photo photo--garden row-a" role="img" aria-label="Quarry enclosure over a pool beside a paved path"></div>
  <div class="photo photo--terrace row-b" role="img" aria-label="Quarry enclosure by a patio with a table"></div>
  <div class="photo photo--pool row-c" role="img" aria-label="Quarry enclosure with red frame over a turquoise pool"></div>

  <footer class="footer">
    <span class="page-no page-no--left">10</span>
    <span class="page-no page-no--right">11</span>
    <div class="brand-mark"><span>Lagoon Canopy NZ</span><span class="dot"></span></div>
  </footer>
</section>

<!-- Vale Shelters spread -->
<section class="spread spread--vale" aria-label="Vale Shelters spread">
  <div class="header-band"></div>
  <div class="title-tab"></div>
  <h2 class="page-title page-title--stacked"><span class="light">Vale</span>Shelters</h2>

  <div class="photo photo--pool hero" role="img" aria-label="Wall-mounted enclosure over an indoor-style pool with sun loungers"></div>
  <div class="photo photo--terrace side-top" role="img" aria-label="Lean-on-wall enclosure over a dining terrace"></div>

  <div class="info-box">
    <h3 class="info-title">Vale Shelters</h3>
    <p class="info-text">We also offer <b>less common types</b> of enclosures. Enclosures <b>for pools in snow-free areas, spa enclosures, lean on wall</b> enclosures, <b>enclosures for large pools, car</b> or <b>boat</b> enclosures.</p>
  </div>

  <div class="photo photo--garden vale-mid" role="img" aria-label="Large enclosure over a long pool on a timber deck"></div>
  <div class="photo photo--garden row-a" role="img" aria-label="Spa enclosure in a brick courtyard"></div>
  <div class="photo photo--terrace row-b" role="img" aria-label="Curved car shelter over a white vehicle"></div>
  <div class="photo photo--water row-c" role="img" aria-label="Boat shelter over a jetty on a lake"></div>

  <footer class="footer">
    <span class="page-no page-no--left">14</span>
    <span class="page-no page-no--right">15</span>
    <div class="brand-mark"><span>Lagoon Canopy NZ</span><span class="dot"></span></div>
  </footer>
</section>

</body>
</html>
```